Helicopter company requires newspaper ad

"Ridgeline Aviators" is an agricultural helicopter company based in Victoria, Australia. We need an advert design for use in newspapers and also possibly social media. Our company specialises in using a helicopter for various agricultural work such as Spraying weeds ("Cropdusting"), spreading fertiliser. This advert will be targeted at farmers in our service area, Our customers are mainly dairy and cow farmers and our services are aimed at increasing their farm productivity. The final design should inform potential and existing customers about our services and the benefits of them. I will attach files of our logo and some existing advertising material for guidance. We would like the ad to feature the blue and green colours in our logo Please feel free to view our website and facebook page to see more about what we do. www.ridgelineaviators.com.au Some text we would like included Spraying: -Accurate -Time Efficient -Zero crop damage -Cost efficient Fertiliser Spreading: -Accurate, Pattern-tested equipment -Zero crop damage or wheel marks -Ability to load product out of a truck, bin or bulk bags -Cost effective, Prices from $32 per hectare depending on spread rate The final advert size should be 195 mm wide x 186 mm high Thanks :)

Target Market(s)

Farmers, Agriculture Industry

Industry/Entity Type

Agribusiness

Colors

Designer to choose colors to be used in the design.

Requirements
Must have
• Phone number 0491 635 087
• The text included in the decription, or variations of this

```html
<!DOCTYPE html>
<html lang="en">
<head>
<meta charset="utf-8">
<title>Ridgeline Aviators – Summer Crops Advert</title>
<link rel="stylesheet" href="https://fonts.googleapis.com/css2?family=Montserrat:wght@700;800&family=Source+Sans+3:wght@400;600;700&display=swap">
<style>
  :root{
    --brand-blue:#1c6db6;
    --brand-navy:#0f2c52;
    --list-blue:#2a78c2;
    --brand-green:#8cc63f;
    --bar-blue:#1f72b8;
    --white:#ffffff;
    --pale:#f1f5f7;
  }
  *{margin:0;padding:0;box-sizing:border-box}
  html,body{width:1200px;height:1104px;overflow:hidden;background:var(--white)}
  .advert{position:relative;width:1200px;height:1104px;overflow:hidden;font-family:"Source Sans 3",Arial,sans-serif}
  .advert__scenery{position:absolute;inset:0;width:1200px;height:1104px}

  .brand{position:absolute;left:48px;top:92px;display:flex;align-items:center;gap:16px}
  .brand__dot{width:34px;height:34px;border-radius:50%;background:var(--brand-green)}
  .brand__name{font-family:"Montserrat",Arial,sans-serif;font-weight:800;font-size:40px;color:var(--white);letter-spacing:.5px}

  .headline{position:absolute;left:40px;top:316px;font-family:"Montserrat",Arial,sans-serif;font-weight:800;font-size:44px;line-height:60px;color:var(--white);letter-spacing:.5px}

  .price-badge{position:absolute;left:32px;top:500px;width:240px;height:240px}
  .price-badge__shape{position:absolute;inset:0;width:240px;height:240px}
  .price-badge__text{position:absolute;inset:0;display:flex;flex-direction:column;align-items:center;justify-content:center;color:var(--white);font-size:21px;line-height:30px;text-align:center}
  .price-badge__amount{font-weight:700;font-size:22px}

  .service{position:absolute;top:756px}
  .service--spreading{left:62px}
  .service--spraying{left:800px}
  .service__title{font-family:"Montserrat",Arial,sans-serif;font-weight:800;font-size:35px;color:var(--brand-blue);margin-bottom:6px;letter-spacing:.3px}
  .service__list{list-style:none}
  .service__item{display:flex;align-items:center;gap:12px;height:42px;font-size:26px;color:var(--list-blue)}
  .tick{width:26px;height:26px;flex:none}

  .contact-bar{position:absolute;left:0;bottom:0;width:1200px;height:71px}
  .contact-bar__bg{position:absolute;inset:0;width:1200px;height:71px}
  .contact-bar__web{position:absolute;left:72px;top:0;height:71px;display:flex;align-items:center;color:var(--white);font-size:29px}
  .contact-bar__call{position:absolute;right:48px;top:0;height:71px;display:flex;align-items:center;gap:16px;color:var(--white)}
  .contact-bar__offer{font-size:32px}
  .contact-bar__phone{font-weight:700;font-size:38px;letter-spacing:.5px}
  .phone-icon{width:40px;height:40px;flex:none}
</style>
</head>
<body>
<main class="advert">
  <svg class="advert__scenery" viewBox="0 0 1200 1104">
    <defs>
      <linearGradient id="sky" x1="0" y1="0" x2="0" y2="1">
        <stop offset="0" stop-color="#2a5ea6"/>
        <stop offset=".5" stop-color="#6f9fd6"/>
        <stop offset=".58" stop-color="#a9c6e4"/>
        <stop offset=".62" stop-color="#6f8f4a"/>
        <stop offset="1" stop-color="#3f6b25"/>
      </linearGradient>
      <linearGradient id="shade" x1="0" y1="0" x2="1" y2="0">
        <stop offset="0" stop-color="#0f2c52" stop-opacity=".95"/>
        <stop offset=".35" stop-color="#1a3f6c" stop-opacity=".6"/>
        <stop offset=".65" stop-color="#1a3f6c" stop-opacity="0"/>
      </linearGradient>
      <linearGradient id="paleField" x1="0" y1="0" x2="0" y2="1">
        <stop offset="0" stop-color="#f7f9fa"/>
        <stop offset=".5" stop-color="#e8eef1"/>
        <stop offset="1" stop-color="#eef2f0"/>
      </linearGradient>
    </defs>
    <g role="img" aria-label="Photo of a helicopter spreading fertiliser from a hanging bucket over green hilly pasture with trees under a blue sky">
      <rect width="1200" height="720" fill="url(#sky)"/>
      <rect width="1200" height="720" fill="url(#shade)"/>
    </g>
    <path d="M0,640 C150,560 300,500 460,540 C660,590 760,690 960,660 C1090,640 1160,600 1200,575 L1200,1104 L0,1104 Z" fill="var(--brand-green)"/>
    <g role="img" aria-label="Faded photo of a spraying helicopter with boom flying low over a crop field">
      <path d="M0,664 C150,584 300,526 460,566 C660,616 760,712 960,682 C1090,662 1160,624 1200,600 L1200,1104 L0,1104 Z" fill="url(#paleField)"/>
    </g>
  </svg>

  <header class="brand">
    <span class="brand__dot"></span>
    <span class="brand__name">Ridgeline Aviators</span>
  </header>

  <h1 class="headline">SUMMER CROPS NEED<br>SPRAYING OR FERTILISER?</h1>

  <div class="price-badge">
    <svg class="price-badge__shape" viewBox="0 0 240 240" aria-hidden="true">
      <polygon fill="var(--brand-blue)" points="234,120 219.1,133.1 230.1,149.5 212.4,158.3 218.7,177 199.3,180.9 200.6,200.6 180.9,199.3 177,218.7 158.3,212.4 149.5,230.1 133.1,219.1 120,234 106.9,219.1 90.5,230.1 81.7,212.4 63,218.7 59.1,199.3 39.4,200.6 40.7,180.9 21.3,177 27.6,158.3 9.9,149.5 20.9,133.1 6,120 20.9,106.9 9.9,90.5 27.6,81.7 21.3,63 40.7,59.1 39.4,39.4 59.1,40.7 63,21.3 81.7,27.6 90.5,9.9 106.9,20.9 120,6 133.1,20.9 149.5,9.9 158.3,27.6 177,21.3 180.9,40.7 200.6,39.4 199.3,59.1 218.7,63 212.4,81.7 230.1,90.5 219.1,106.9"/>
    </svg>
    <div class="price-badge__text">
      <span>Prices from</span>
      <span class="price-badge__amount">$32 PER HECTARE</span>
      <span>depending on</span>
      <span>spread rate</span>
    </div>
  </div>

  <svg width="0" height="0" style="position:absolute" aria-hidden="true">
    <symbol id="tick" viewBox="0 0 26 26">
      <circle cx="13" cy="13" r="10.5" fill="none" stroke="var(--list-blue)" stroke-width="2.2"/>
      <path d="M8 13.2l3.6 3.6L19 9" fill="none" stroke="var(--list-blue)" stroke-width="2.6" stroke-linecap="round" stroke-linejoin="round"/>
    </symbol>
  </svg>

  <section class="service service--spreading">
    <h2 class="service__title">SPREADING</h2>
    <ul class="service__list">
      <li class="service__item"><svg class="tick"><use href="#tick"/></svg>Accurate</li>
      <li class="service__item"><svg class="tick"><use href="#tick"/></svg>Pattern-tested equipment</li>
      <li class="service__item"><svg class="tick"><use href="#tick"/></svg>Zero crop damage or wheel marks</li>
      <li class="service__item"><svg class="tick"><use href="#tick"/></svg>Ability to load product out of a truck, bin or bulk bags</li>
      <li class="service__item"><svg class="tick"><use href="#tick"/></svg>Cost effective</li>
    </ul>
  </section>

  <section class="service service--spraying">
    <h2 class="service__title">SPRAYING</h2>
    <ul class="service__list">
      <li class="service__item"><svg class="tick"><use href="#tick"/></svg>Accurate</li>
      <li class="service__item"><svg class="tick"><use href="#tick"/></svg>Time Efficient</li>
      <li class="service__item"><svg class="tick"><use href="#tick"/></svg>Zero crop damage</li>
      <li class="service__item"><svg class="tick"><use href="#tick"/></svg>Cost efficient Fertiliser</li>
    </ul>
  </section>

  <footer class="contact-bar">
    <svg class="contact-bar__bg" viewBox="0 0 1200 71" aria-hidden="true">
      <rect width="1200" height="71" fill="var(--brand-green)"/>
      <path d="M0,0 H522 L500,71 H0 Z" fill="var(--bar-blue)"/>
    </svg>
    <span class="contact-bar__web">www.ridgelineaviators.com.au</span>
    <div class="contact-bar__call">
      <span class="contact-bar__offer">FREE estimate!</span>
      <svg class="phone-icon" viewBox="0 0 40 40" aria-hidden="true">
        <circle cx="20" cy="20" r="17" fill="none" stroke="#fff" stroke-width="3"/>
        <path d="M14 11.5c1-.6 2-.3 2.5.6l1.6 3c.4.8.2 1.6-.5 2.1l-1.3 1c.9 2.2 2.6 4 4.8 5l1-1.3c.5-.7 1.4-.9 2.1-.5l3 1.6c.9.5 1.2 1.6.6 2.5l-1 1.6c-.8 1.2-2.3 1.7-3.7 1.2-5.2-1.8-9.3-5.9-11-11.1-.5-1.4 0-2.9 1.2-3.7z" fill="#fff"/>
      </svg>
      <span class="contact-bar__phone">0491 635 087</span>
    </div>
  </footer>
</main>
</body>
</html>
```